Maple Row Yardcare

I want it as prefession and attractive as possible we are a lawnmowing business

Phone number 605-318-2264
Name- Carl Whitby
Email- mapleroweyardsd@fernpost.net

```html
<!DOCTYPE html>
<html lang="en">
<head>
<meta charset="utf-8">
<title>Maple Row Yardcare – Business Card</title>
<link rel="stylesheet" href="https://fonts.googleapis.com/css2?family=Montserrat:wght@400;500;800&display=swap">
<style>
  :root {
    --backdrop: #ecebe6;
    --card-front: #fbfbfa;
    --card-back: #0f4a2a;
    --card-back-light: #17603a;
    --card-back-dark: #0b3d22;
    --brand-green: #1e6b34;
    --accent-green: #4cb043;
    --ink: #1c1c1c;
    --white: #ffffff;
  }
  * { margin: 0; padding: 0; box-sizing: border-box; }
  html, body {
    width: 1200px;
    height: 692px;
    overflow: hidden;
    background: var(--backdrop);
    font-family: "Montserrat", Arial, sans-serif;
  }
  .stage {
    position: relative;
    width: 1200px;
    height: 692px;
  }
  .card {
    position: absolute;
    top: 183px;
    width: 526px;
    height: 327px;
    border-radius: 14px;
    box-shadow: 0 4px 14px rgba(0, 0, 0, 0.18);
    overflow: hidden;
  }
  .card--front {
    left: 56px;
    background: var(--card-front);
  }
  .card--back {
    left: 620px;
    background: var(--card-back);
  }
  .back-texture {
    position: absolute;
    inset: 0;
    background:
      radial-gradient(ellipse at 50% 50%, var(--card-back-light) 0%, rgba(23, 96, 58, 0) 60%),
      linear-gradient(160deg, var(--card-back) 0%, var(--card-back-dark) 100%);
  }
  .brand-lockup {
    position: absolute;
    display: flex;
    align-items: center;
    gap: 14px;
  }
  .card--front .brand-lockup {
    left: 100px;
    top: 36px;
    width: 330px;
    height: 110px;
  }
  .card--back .brand-lockup {
    left: 93px;
    top: 106px;
    width: 341px;
    height: 112px;
  }
  .brand-mark {
    flex: none;
    width: 20px;
    height: 20px;
    background: var(--accent-green);
  }
  .brand-name {
    font-weight: 800;
    font-size: 35px;
    letter-spacing: 0.5px;
    text-transform: uppercase;
    line-height: 1.08;
    color: var(--brand-green);
  }
  .card--back .brand-name {
    color: var(--white);
  }
  .holder-name {
    position: absolute;
    left: 0;
    right: 0;
    top: 170px;
    text-align: center;
    font-weight: 400;
    font-size: 27px;
    color: var(--ink);
  }
  .contact-list {
    position: absolute;
    left: 0;
    right: 0;
    top: 225px;
    list-style: none;
    display: flex;
    flex-direction: column;
    align-items: center;
    gap: 10px;
  }
  .contact-item {
    display: flex;
    align-items: center;
    gap: 10px;
    font-size: 18px;
    font-weight: 500;
    color: var(--ink);
  }
  .contact-icon {
    width: 22px;
    height: 22px;
    flex: none;
  }
</style>
</head>
<body>
  <main class="stage">
    <section class="card card--front" aria-label="Card front">
      <div class="brand-lockup">
        <span class="brand-mark" aria-hidden="true"></span>
        <h1 class="brand-name">Maple Row<br>Yardcare</h1>
      </div>
      <p class="holder-name">Carl Whitby</p>
      <ul class="contact-list">
        <li class="contact-item">
          <svg class="contact-icon" viewBox="0 0 24 24" aria-hidden="true">
            <path fill="#4cb043" d="M6.6 10.8a15.1 15.1 0 0 0 6.6 6.6l2.2-2.2c.3-.3.7-.4 1-.2 1.1.4 2.3.6 3.6.6.6 0 1 .4 1 1V20c0 .6-.4 1-1 1A17 17 0 0 1 3 4c0-.6.4-1 1-1h3.5c.6 0 1 .4 1 1 0 1.3.2 2.5.6 3.6.1.3 0 .7-.2 1z"/>
            <path fill="none" stroke="#4cb043" stroke-width="1.6" stroke-linecap="round" d="M14.5 3.5a6.5 6.5 0 0 1 6 6M14.5 7a3 3 0 0 1 2.6 2.6"/>
          </svg>
          <span>605-318-2264</span>
        </li>
        <li class="contact-item">
          <svg class="contact-icon" viewBox="0 0 24 24" aria-hidden="true">
            <rect x="2" y="5" width="20" height="14" rx="1" fill="#4cb043"/>
            <path d="M2.5 5.8 12 13l9.5-7.2" fill="none" stroke="#fbfbfa" stroke-width="1.6"/>
          </svg>
          <span>mapleroweyardsd@fernpost.net</span>
        </li>
      </ul>
    </section>

    <section class="card card--back" aria-label="Card back">
      <div class="back-texture" role="img" aria-label="Faint repeating brand pattern on deep green"></div>
      <div class="brand-lockup">
        <span class="brand-mark" aria-hidden="true"></span>
        <p class="brand-name">Maple Row<br>Yardcare</p>
      </div>
    </section>
  </main>
</body>
</html>
```